Showroom Signage Design – Bright Hinges (High-Exposure Road Frontage)

Project Overview
We are looking for a creative designer to develop large-scale external signage for the Bright Hinges showroom.
The building is a double-storey showroom with full glass frontage positioned on a very busy main road.
The glazing spans both levels and we want to utilise the façade like a large billboard that captures attention from passing traffic.
The design must be bold, clean, professional, and highly readable at speed.
About Bright Hinges:
Bright Hinges specialises in cabinetry face-lifts / renovations.
including:
Our Core Service — Cabinetry Facelifts
- Kitchens
- Bathrooms
- Laundries
- Wardrobes
We Also Offer New Installations:
- Kitchens
- Bathrooms
- Laundries
- Wardrobes
We want the signage to clearly communicate that we are experts in facelifting / renovating spaces, while also providing complete new cabinetry solutions.
We will remove the reflective film on the windows for the lower level. There will be a kitchen showing in the middle of the lower level. So we don't want signage infront of the kitchen area. (Attached is a screenshot of the office with blue and pink squares. The blue is the location of the kitchen internally, and the pink can be signage design spaces.) Ideally the printing wont have a solid colour background for printing on the lower level.
Design Goals:
- Turns the entire glazed frontage into a visual billboard
- Works across two storeys
- Is highly visible from passing vehicles
- Uses strong hierarchy and minimal clutter
- Clearly communicates our services at a glance
- Encourages customers to visit the showroom
Think impact first, then detail.
Key Considerations
- Viewed primarily by drive-by traffic
- Must read clearly from distance and speed
- Should utilise window graphics, scale, and layout effectively
- Design should enhance — not block — natural light where possible
- Must feel architectural and professional, not retail clutter
Deliverables:
Print-ready vector files (AI/EPS/PDF)
Building mockups showing real-world application
We are looking for a design that makes Bright Hinges impossible to miss — transforming the showroom frontage into a powerful advertising statement.
Target Market(s)
Renovation clients on a budget, but also clients wanting an efficient turn around of high end projects.
Colors
Designer to choose only greyscale colors for use in the design.
Look and feel

```html
<!DOCTYPE html>
<html lang="en">
<head>
<meta charset="utf-8">
<title>Bright Hinges – Showroom Signage</title>
<link rel="stylesheet" href="https://fonts.googleapis.com/css2?family=Montserrat:wght@700;800&family=Oswald:wght@500;600&display=swap">
<style>
  :root {
    --bg: #8e979f;
    --bg-light: #a9b1b8;
    --panel: #5c5e61;
    --panel-edge: #4a4c4f;
    --service-panel: #6b6d70;
    --title-grey: #a3a4a6;
    --ink: #121212;
    --white: #ffffff;
    --bar: #0b0b0b;
    --icon-grey: #9c9da0;
  }
  * { margin: 0; padding: 0; box-sizing: border-box; }
  html, body { width: 1200px; height: 1200px; overflow: hidden; }
  body {
    background: radial-gradient(ellipse at 50% 40%, var(--bg-light), var(--bg) 75%);
    position: relative;
  }
  .signage { position: absolute; inset: 0; }

  .header-sign {
    position: absolute;
    left: 70px; top: 210px;
    width: 1060px; height: 360px;
    background: var(--panel);
    border-bottom: 6px solid var(--panel-edge);
    display: flex;
    align-items: center;
    padding: 0 48px 0 40px;
    gap: 40px;
  }
  .appliance-icons {
    width: 240px; height: 280px;
    flex: none;
    background: linear-gradient(180deg, var(--icon-grey), #8a8b8e);
    border-radius: 4px;
    opacity: .9;
  }
  .header-text {
    flex: 1;
    min-width: 0;
    font-family: "Montserrat", sans-serif;
    text-align: right;
    line-height: 1;
  }
  .brand-name {
    font-weight: 800;
    font-size: 74px;
    color: var(--title-grey);
    letter-spacing: 1px;
    margin-bottom: 26px;
    white-space: nowrap;
  }
  .tagline {
    font-weight: 800;
    font-size: 38px;
    color: var(--ink);
    white-space: nowrap;
    margin-top: 12px;
  }

  .service-block {
    position: absolute;
    top: 610px;
    width: 440px;
  }
  .service-block.left { left: 70px; }
  .service-block.right { right: 70px; }
  .service-panel {
    background: var(--service-panel);
    height: 180px;
    margin: 0 10px;
    padding: 0 20px;
    font-family: "Oswald", sans-serif;
    color: var(--white);
    text-align: center;
    display: flex;
    flex-direction: column;
    justify-content: center;
    gap: 6px;
  }
  .service-label {
    font-weight: 500;
    font-size: 26px;
    display: flex;
    align-items: center;
    justify-content: center;
    gap: 10px;
  }
  .service-label::before, .service-label::after {
    content: "";
    width: 34px; height: 2px;
    background: var(--white);
  }
  .service-title { font-weight: 600; font-size: 34px; line-height: 1.1; white-space: nowrap; }
  .service-list { font-weight: 500; font-size: 14px; letter-spacing: .3px; white-space: nowrap; }
  .info-bar {
    background: var(--bar);
    color: var(--white);
    font-family: "Oswald", sans-serif;
    font-weight: 500;
    font-size: 21px;
    height: 52px;
    display: flex;
    align-items: center;
    padding: 0 28px;
    white-space: nowrap;
  }
  .info-bar.centered { justify-content: center; }
</style>
</head>
<body>
<main class="signage">
  <section class="header-sign">
    <div class="appliance-icons" role="img" aria-label="Grey icon group of kitchen cabinets, rangehood, bathtub and washing machine"></div>
    <div class="header-text">
      <h1 class="brand-name">BRIGHT HINGES</h1>
      <p class="tagline">KITCHEN &amp; HOME FACELIFTS</p>
      <p class="tagline">THE RENOVATION EXPERTS</p>
    </div>
  </section>

  <section class="service-block left">
    <div class="service-panel">
      <p class="service-label">OUR SERVICES</p>
      <h2 class="service-title">FACELIFTS &amp; RENOVATIONS</h2>
      <p class="service-list">KITCHENS • BATHROOMS • LAUNDRIES • WARDROBES</p>
    </div>
    <p class="info-bar centered">VISIT OUR SHOWROOM • WALK-INS WELCOME</p>
  </section>

  <section class="service-block right">
    <div class="service-panel">
      <p class="service-label">WE ALSO OFFER</p>
      <h2 class="service-title">NEW INSTALLATIONS</h2>
      <p class="service-list">KITCHENS • BATHROOMS • LAUNDRIES • WARDROBES</p>
    </div>
    <p class="info-bar">OPEN MON-SAT • [WEB ADDRESS]</p>
  </section>
</main>
</body>
</html>
```